Fish Farm needing 3 - Fold Flyer / Price List designed

We are looking for a new Price List for our Fish Farm. I have attached an example of the basic info that needs in the flyer. We want the flyer to be a 3 fold page. Anything that is on our website, you can use for ideas. There are some pictures on there that can be photoshopped into the flyer. Do not use any photos from any other sites. We are looking for something professional but fun and exciting! I have also attached our business logo. We tend to stay with the blues and greens for colors. Let's get started....
Updates

Need extra days to review

Contact Information for Business Card

We are needing a business card with our new logo on it. We also need our address, phone numbers, email address, and website listed. Please view our website for more ideas.

Colors

Designer to choose colors to be used in the design.

```html
<!DOCTYPE html>
<html lang="en">
<head>
<meta charset="utf-8">
<title>Fish Farm Price List – Tri-fold</title>
<link href="https://fonts.googleapis.com/css2?family=Oswald:wght@500;700&family=Lato:wght@400;700&family=Libre+Baskerville:ital,wght@1,700&display=swap" rel="stylesheet">
<style>
  :root{
    --bg:#3cb4ee;
    --paper:#f4f5f7;
    --navy:#0b2a5c;
    --deep:#071c3f;
    --royal:#1a57a8;
    --sky:#3a9be0;
    --ink:#2a3340;
    --rule:#1d4f9a;
  }
  *{box-sizing:border-box;margin:0;padding:0}
  html,body{width:1200px;height:816px;overflow:hidden}
  body{background:var(--bg);font-family:"Lato",Arial,sans-serif;color:var(--ink)}
  .brochure{position:absolute;left:30px;top:28px;width:1140px;height:760px;background:var(--paper);overflow:hidden;box-shadow:0 18px 40px rgba(0,40,80,.35)}
  .fold{position:absolute;top:0;bottom:0;width:1px;background:rgba(0,0,0,.07)}
  .decor{position:absolute;left:0;top:0}
  .photo{position:absolute;border-radius:50%;border:6px solid #fff;box-shadow:0 4px 10px rgba(0,0,0,.25)}
  .photo-ring{position:absolute;border-radius:50%;border:2px dashed var(--royal)}
  .item{position:absolute;width:270px}
  .item h2{font-family:"Oswald",sans-serif;font-weight:700;font-size:17px;color:var(--navy);text-transform:uppercase;letter-spacing:.2px;line-height:1}
  .item h2 small{font-family:"Lato",sans-serif;font-weight:400;font-size:10px;color:var(--sky);text-transform:none;margin-left:4px}
  .item .sub{display:block;font-family:"Oswald",sans-serif;font-weight:500;font-size:9px;color:var(--sky);text-transform:uppercase;text-align:right;margin-top:1px}
  .price-table{width:100%;border-collapse:collapse;margin-top:3px;border:1.5px solid var(--rule);border-top:none;background:#fff}
  .price-table th{background:linear-gradient(90deg,var(--royal),var(--navy));color:#fff;font-family:"Oswald",sans-serif;font-weight:500;font-size:10px;padding:2px 6px;text-align:left}
  .price-table td{font-size:10.5px;padding:1px 6px;color:var(--ink)}
  .price-table tr:last-child td{padding-bottom:5px}
  .price-table tr:nth-child(2) td{padding-top:4px}
  .emblem{position:absolute;width:40px;height:56px;border-radius:50%;background:linear-gradient(160deg,var(--sky),var(--royal) 60%,var(--navy))}
  .emblem.lg{width:48px;height:66px}
  .note{position:absolute;font-family:"Libre Baskerville",serif;font-style:italic;font-weight:700;color:var(--royal);font-size:14px;text-align:center;line-height:1.35}
  .dark-copy{position:absolute;color:#fff;font-size:11px;line-height:1.35}
  .dark-copy h3{font-family:"Oswald",sans-serif;font-weight:700;font-size:16px;color:var(--sky);text-transform:uppercase}
  .feed{position:absolute;font-size:11px;line-height:1.4;color:var(--ink)}
  .feed h2{font-family:"Oswald",sans-serif;font-weight:700;font-size:17px;color:var(--navy);text-transform:uppercase}
  .closing{position:absolute;left:800px;top:640px;font-family:"Oswald",sans-serif;text-transform:uppercase;font-size:17px;line-height:1.25}
  .closing .lead{color:#fff}
  .closing .warn{color:var(--sky)}
</style>
</head>
<body>
<main class="brochure">
  <svg class="decor" width="1140" height="760" viewBox="0 0 1140 760">
    <path d="M0 0 H380 V40 C330 150 230 185 120 180 C70 178 30 168 0 150Z" fill="#e7ebf1"/>
    <path d="M0 150 C60 200 200 210 300 150 C250 205 120 225 0 200Z" fill="var(--navy)"/>
    <path d="M0 175 C80 215 210 215 320 140 C240 220 110 240 0 215Z" fill="var(--royal)"/>
    <path d="M0 760 L0 690 C120 735 270 750 400 680 C440 660 455 560 505 548 C545 540 550 605 600 612 C680 625 720 560 760 540 C860 492 1000 520 1140 420 L1140 760Z" fill="var(--deep)"/>
    <path d="M760 540 C860 492 1000 520 1140 420 L1140 400 C1010 500 860 470 760 520Z" fill="var(--royal)"/>
  </svg>

  <div class="fold" style="left:380px"></div>
  <div class="fold" style="left:760px"></div>

  <!-- Panel 1 -->
  <div role="img" aria-label="Photo of a worker netting fish in a pond" style="position:absolute;left:0;top:0;width:270px;height:165px;border-bottom-right-radius:140px 110px;background:linear-gradient(135deg,#6f8a5a,#4d6a75 60%,#8ba07a)"></div>
  <div class="photo" role="img" aria-label="Photo of water spraying onto a grassy pond bank" style="left:225px;top:-20px;width:105px;height:105px;background:linear-gradient(160deg,#7fa25c,#4f7a3c)"></div>

  <section class="item" style="left:95px;top:250px;width:250px">
    <h2 style="text-align:right">Hybrid Bluegill</h2>
    <span class="sub">(Hybrid Sunfish)</span>
    <table class="price-table"><tr><th>Size</th><th>Each</th><th>1000</th><th>3000</th></tr>
      <tr><td>1-3 Inch</td><td>50¢</td><td>45¢</td><td>40¢</td></tr>
      <tr><td>3-5 Inch</td><td>80¢</td><td>75¢</td><td></td></tr>
      <tr><td>*5-7 Inch</td><td>$1.75</td><td></td><td></td></tr></table>
  </section>
  <div class="emblem" role="img" aria-label="Fish emblem" style="left:52px;top:272px"></div>

  <section class="item" style="left:30px;top:360px;width:250px">
    <h2>Regular Bluegill</h2>
    <table class="price-table"><tr><th>Size</th><th>Each</th><th>1000</th></tr>
      <tr><td>1-3 Inch</td><td>50¢</td><td>45¢</td></tr>
      <tr><td>*3-5 Inch</td><td>80¢</td><td>75¢</td></tr></table>
  </section>
  <div class="emblem" role="img" aria-label="Fish emblem" style="left:292px;top:364px"></div>

  <section class="item" style="left:95px;top:455px;width:250px">
    <h2 style="text-align:right">Redear Sunfish</h2>
    <table class="price-table"><tr><th>Size</th><th>Each</th><th>1000</th></tr>
      <tr><td>1-3 Inch</td><td>50¢</td><td>45¢</td></tr>
      <tr><td>3-4 Inch</td><td>75¢</td><td>70¢</td></tr>
      <tr><td>*4-5 Inch</td><td>$1.00</td><td>95¢</td></tr></table>
  </section>
  <div class="emblem" role="img" aria-label="Fish emblem" style="left:50px;top:472px"></div>

  <section class="item" style="left:30px;top:560px;width:270px">
    <h2>Largemouth Bass</h2>
    <table class="price-table"><tr><th>Size</th><th>Each</th><th>Size</th><th>Each</th></tr>
      <tr><td>3 Inch</td><td>$1.10</td><td>*4-6 Inch</td><td>$1.95</td></tr>
      <tr><td>3-4 Inch</td><td>$1.20</td><td>*6-8 Inch</td><td>$2.75</td></tr></table>
  </section>
  <div class="emblem" role="img" aria-label="Fish emblem" style="left:312px;top:562px"></div>

  <p class="note" style="left:60px;top:650px;width:280px">*When Available.<br>Sizes Vary Depending on<br>Time of Year</p>

  <!-- Panel 2 -->
  <section class="item" style="left:450px;top:40px;width:260px">
    <h2 style="text-align:right">Triploid Grass Carp</h2>
    <span class="sub" style="text-transform:none;font-family:Lato,sans-serif;font-weight:400">(Indiana Prices)</span>
    <table class="price-table"><tr><th>Size</th><th>Each</th></tr>
      <tr><td>8-11 Inch</td><td>Minimum 5</td></tr>
      <tr><td>5-24 Grass Carp</td><td>$16.00 each</td></tr>
      <tr><td>25-49 Grass Carp</td><td>$15.00 each</td></tr>
      <tr><td>50-99 Grass Carp</td><td>$14.00 each</td></tr>
      <tr><td>100+ Grass Carp</td><td>Inquire</td></tr></table>
  </section>
  <div class="emblem lg" role="img" aria-label="Fish emblem" style="left:400px;top:84px"></div>

  <section class="item" style="left:410px;top:200px;width:230px">
    <h2>Channel Catfish</h2>
    <table class="price-table"><tr><th>Size</th><th>Each</th><th>1000</th></tr>
      <tr><td>6-8 Inch</td><td>65¢</td><td>60¢</td></tr></table>
  </section>
  <div class="emblem" role="img" aria-label="Fish emblem" style="left:657px;top:197px"></div>

  <section class="item" style="left:470px;top:280px;width:250px">
    <h2 style="text-align:right">Albino Catfish <small>(March &amp; April)</small></h2>
    <table class="price-table"><tr><th>Size</th><th>Each</th></tr>
      <tr><td>5-8 Inch</td><td>$1.20</td></tr></table>
  </section>
  <div class="emblem" role="img" aria-label="Fish emblem" style="left:422px;top:287px"></div>

  <section class="item" style="left:415px;top:365px;width:240px">
    <h2>Black Crappie <small>(March &amp; April)</small></h2>
    <table class="price-table"><tr><th>Size</th><th>Each</th></tr>
      <tr><td>3-5 Inch</td><td>$1.10</td></tr></table>
  </section>
  <div class="emblem" role="img" aria-label="Fish emblem" style="left:667px;top:357px"></div>

  <div class="photo" role="img" aria-label="Photo of a farmer holding a large golden koi" style="left:555px;top:565px;width:125px;height:125px;background:linear-gradient(160deg,#3a6ea8,#2a4f7a 50%,#c98a2c)"></div>
  <div class="photo-ring" style="left:567px;top:577px;width:101px;height:101px"></div>
  <div role="img" aria-label="Photo of dark koi swimming" style="position:absolute;left:640px;top:520px;width:56px;height:56px;border-radius:50%;background:linear-gradient(135deg,#2b5f9e,#0d2a55)"></div>

  <div class="dark-copy" style="left:410px;top:690px">
    <h3>Fathead Minnows</h3>
    $36.00 per thousand<br>($9.00 per lb.)
  </div>

  <!-- Panel 3 -->
  <section class="item" style="left:790px;top:30px;width:230px">
    <h2>Golden Shiners</h2>
    <table class="price-table"><tr><th>(Delivery Only – Minimum 50 lb.)</th><th></th></tr>
      <tr><td>50-99 lb.</td><td>$8.00 lb.</td></tr>
      <tr><td>100+ lb.</td><td>$7.50 lb.</td></tr></table>
  </section>
  <div class="emblem" role="img" aria-label="Fish emblem" style="left:1032px;top:30px"></div>

  <section class="item" style="left:850px;top:120px;width:250px">
    <h2>Tilapia <small>(May 15 – June 30)</small></h2>
    <table class="price-table"><tr><th>Size</th><th>Each</th></tr>
      <tr><td>5-10</td><td>Tilapia per lb.</td></tr>
      <tr><td>1-25 lb.</td><td>$15.00 lb.</td></tr>
      <tr><td>26-40 lb.</td><td>$14.00 lb.</td></tr>
      <tr><td>40-50 lb.</td><td>$13.00 lb.</td></tr>
      <tr><td>50+ lb.</td><td>$12.00 lb.</td></tr></table>
  </section>
  <div class="emblem lg" role="img" aria-label="Fish emblem" style="left:797px;top:152px"></div>

  <section class="item" style="left:790px;top:265px;width:230px">
    <h2>Japanese Koi</h2>
    <table class="price-table"><tr><th>Size</th><th>Each</th></tr>
      <tr><td>4-5 Inch</td><td>$6.00</td></tr>
      <tr><td>6-8 Inch</td><td>$10.00</td></tr>
      <tr><td>*9-12 Inch</td><td>$15.00</td></tr></table>
  </section>
  <div class="emblem" role="img" aria-label="Fish emblem" style="left:1032px;top:247px"></div>

  <div class="feed" style="left:790px;top:400px">
    <h2>Floating Fish Food</h2>
    Starter Size (50 lb. Bag)<br>41% Protein<br>Market Price – Inquire<br>(Only Available at Farm)
  </div>

  <div role="img" aria-label="Underwater photo of a shark" style="position:absolute;left:1050px;top:330px;width:110px;height:230px;border-top-left-radius:110px 115px;border-bottom-left-radius:110px 115px;background:linear-gradient(160deg,#6fb4e6,#1f6fb8 60%,#0d3f7a)"></div>
  <div class="photo" role="img" aria-label="Photo of a farmer holding a large catfish" style="left:955px;top:360px;width:112px;height:112px;background:linear-gradient(160deg,#6d8a4c,#3a6aa0 60%,#b9b2a0)"></div>
  <div class="photo-ring" style="left:966px;top:371px;width:90px;height:90px"></div>

  <div class="closing">
    <div class="lead">Butterfly Koi<br>Also Available!</div>
    <div class="warn">Prices Subject to<br>Change Without Notice</div>
  </div>
</main>
</body>
</html>
```